Dynamic Business Card for Sports Supplements Company

Hi! I'm looking for an awesome business card to match my existing sports supplement company. I have uploaded my current company logo and screenshot of the front page of my website.

I would like to have something dynamic and interesting and utilize the colors in the website - the reds and purples

The business card should be double sided and focus on a unique eye-catching design on the back and include all the relevant company info.

Most importantly, it should say somewhere: "Sign up on our website for a coupon code."

Target Market(s)

Mostly for women gym goers but it shouldn't be too feminine. It should be in keeping with the website design. It should flow and clearly be connected to it

Industry/Entity Type

Business

Contact Information for Business Card

Colleen M. Varga
CEO
CVarga@Vitalorexco.example
www.vitalorexco.example
555.014.3827
P.O. Box 48317
Larkfield, Ohio 00000

Sign up on our website for a coupon code

Font styles to use
Serif
Sans Serif
Other font styles liked:
• Novecento font family and "Vitalorex" is in AR Destine font

Requirements
Must have
• One side should be a bold Vitalorex logo design. Even just the symbol itself may be o.k. (see attached file)

```html
<!DOCTYPE html>
<html lang="en">
<head>
<meta charset="utf-8">
<title>Vitalorex Business Card</title>
<link href="https://fonts.googleapis.com/css2?family=Montserrat:wght@700;800&family=Open+Sans:wght@400;600&display=swap" rel="stylesheet">
<style>
  :root {
    --ink: #0d0d0d;
    --red: #e41e26;
    --white: #ffffff;
    --grey: #3a3a3a;
    --tag-grey: #9a9a9a;
    --page: #ecebe8;
  }
  * { margin: 0; padding: 0; box-sizing: border-box; }
  html, body { width: 1200px; height: 950px; overflow: hidden; background: var(--page); }
  .stage { position: relative; width: 1200px; height: 950px; }

  .card {
    position: absolute; top: 115px; width: 420px; height: 720px;
    overflow: hidden; box-shadow: 0 10px 28px rgba(0,0,0,.18);
  }
  .card--front { left: 150px; background: var(--white); }
  .card--back { left: 630px; background: var(--red); }

  .front-bg { position: absolute; inset: 0; width: 420px; height: 720px; }

  .brand { position: absolute; left: 0; right: 0; top: 150px; text-align: center; }
  .brand__row { display: inline-flex; align-items: center; gap: 12px; }
  .brand__dot { width: 20px; height: 20px; border-radius: 50%; background: var(--red); }
  .brand__name {
    font-family: "Montserrat", sans-serif; font-weight: 800; font-size: 44px;
    letter-spacing: 2px; color: var(--white); text-transform: uppercase;
  }
  .brand__tagline {
    margin-top: 6px; font-family: "Open Sans", sans-serif; font-size: 13px;
    letter-spacing: 3.5px; color: var(--tag-grey); text-transform: uppercase;
  }

  .contact {
    position: absolute; left: 0; right: 0; top: 430px; text-align: center;
    font-family: "Open Sans", sans-serif; color: var(--grey);
  }
  .contact__name {
    font-family: "Montserrat", sans-serif; font-weight: 700; font-size: 24px;
    letter-spacing: 1.5px; color: var(--red); text-transform: uppercase;
  }
  .contact__title { font-size: 17px; margin-bottom: 14px; }
  .contact__line { font-size: 17px; line-height: 25px; }
  .contact__list { margin-top: 10px; display: inline-block; text-align: left; }
  .contact__item { display: flex; align-items: center; gap: 8px; font-size: 17px; line-height: 27px; }
  .contact__icon { width: 16px; height: 16px; flex: none; }

  .emblem {
    position: absolute; left: 70px; top: 200px; width: 280px; height: 280px;
    border-radius: 50%; background: var(--ink);
    display: flex; align-items: center; justify-content: center;
  }
  .emblem__name {
    font-family: "Montserrat", sans-serif; font-weight: 800; font-size: 38px;
    letter-spacing: 2px; color: var(--white); text-transform: uppercase;
  }
  .promo {
    position: absolute; left: 0; right: 0; bottom: 52px; text-align: center;
    font-family: "Open Sans", sans-serif; font-size: 16px; letter-spacing: .4px; color: var(--white);
  }
</style>
</head>
<body>
<main class="stage">

  <section class="card card--front" aria-label="Business card front">
    <svg class="front-bg" viewBox="0 0 420 720" aria-hidden="true">
      <polygon points="0,0 420,0 420,270 210,378 0,270" fill="var(--ink)"/>
      <polygon points="0,270 210,378 420,270 420,282 210,392 0,282" fill="var(--red)"/>
    </svg>
    <div class="brand">
      <div class="brand__row">
        <span class="brand__dot"></span>
        <span class="brand__name">Vitalorex</span>
      </div>
      <div class="brand__tagline">Your Training Ally</div>
    </div>
    <div class="contact">
      <div class="contact__name">Colleen M. Varga</div>
      <div class="contact__title">CEO</div>
      <div class="contact__line">P.O. Box 48317</div>
      <div class="contact__line">Larkfield, Ohio 00000</div>
      <div class="contact__list">
        <div class="contact__item">
          <svg class="contact__icon" viewBox="0 0 16 16" aria-hidden="true"><rect x="1" y="3" width="14" height="10" rx="1" fill="var(--red)"/><path d="M1.5 4 8 9l6.5-5" stroke="#fff" stroke-width="1.3" fill="none"/></svg>
          <span>CVarga@Vitalorexco.example</span>
        </div>
        <div class="contact__item">
          <svg class="contact__icon" viewBox="0 0 16 16" aria-hidden="true"><path d="M3.5 1.5 6 4.5 4.6 6.2c.9 2 2.6 3.7 4.6 4.6l1.7-1.4 3 2.5-1.6 2.1C7 13.7 2.3 9 1.4 3.1z" fill="var(--red)"/></svg>
          <span>555.014.3827</span>
        </div>
        <div class="contact__item">
          <svg class="contact__icon" viewBox="0 0 16 16" aria-hidden="true"><circle cx="8" cy="8" r="7" fill="var(--red)"/><path d="M1 8h14M8 1c-3 3.5-3 10.5 0 14M8 1c3 3.5 3 10.5 0 14" stroke="#fff" stroke-width="1" fill="none"/></svg>
          <span>www.vitalorexco.example</span>
        </div>
      </div>
    </div>
  </section>

  <section class="card card--back" aria-label="Business card back">
    <div class="emblem"><span class="emblem__name">Vitalorex</span></div>
    <p class="promo">Sign up on our website for a coupon code</p>
  </section>

</main>
</body>
</html>
```